Plumbing & Heating company

A leaflet containing -

Company name - Brackenfold Plumbing Solutions
logo
Mobile number - 07700 914226
Landline - 01632 870512
Email - Info@brackenfoldplumbing.example.co.uk
website - Brackenfold-plumbing.example.co.uk
Social media logos - pixgram, Chatterly

services we offer

- Boiler replacements (free quote)
- General plumbing & heating
- Tap replacements
- 1st & 2nd
- New builds & Extensions
- Cylinder replcemets

```html
<!DOCTYPE html>
<html lang="en">
<head>
<meta charset="utf-8">
<title>Brackenfold Plumbing Solutions – Leaflet</title>
<link href="https://fonts.googleapis.com/css2?family=Montserrat:wght@400;500;700;800;900&display=swap" rel="stylesheet">
<style>
  :root{
    --backdrop:#f4f4f2;
    --blue-deep:#0b4f98;
    --blue:#1367b4;
    --blue-light:#1b9ad6;
    --orange:#f7931e;
    --orange-deep:#f05a28;
    --yellow:#fbb81c;
    --red:#f23d3d;
    --ink:#1c1c24;
    --white:#ffffff;
  }
  *{box-sizing:border-box;margin:0;padding:0}
  html,body{width:1200px;height:1200px;overflow:hidden;background:var(--backdrop)}
  body{font-family:"Montserrat",Arial,sans-serif;position:relative}
  .leaflet{position:absolute;left:152px;top:20px;width:896px;height:1160px;overflow:hidden;background:var(--white)}
  .leaflet-inner{position:absolute;left:0;top:0;width:1053px;height:1363px;transform:scale(0.851);transform-origin:0 0}
  .artwork{position:absolute;left:0;top:0;width:1053px;height:1363px}
  .brand{position:absolute;left:52px;top:70px;width:240px;color:var(--white);font-weight:800;text-align:center;line-height:1}
  .brand-name{font-size:33px;letter-spacing:1px;display:block}
  .brand-sub{font-size:14.5px;letter-spacing:1.6px;display:block;margin-top:6px}
  .brand-dot{display:block;width:22px;height:22px;border-radius:50%;background:var(--white);margin:0 auto 10px}
  .headline{position:absolute;left:56px;top:206px;color:var(--white);font-size:35px;line-height:43.5px;font-weight:400;letter-spacing:.3px;text-transform:uppercase}
  .headline strong{font-weight:800}
  .photo-frame{position:absolute;border-radius:50%;border:10px solid var(--white);overflow:hidden}
  .photo-frame.boiler{left:134px;top:452px;width:320px;height:320px;background:radial-gradient(circle at 55% 45%,#e9e4dc 0 14%,#b88b60 40%,#8a6140 100%)}
  .photo-frame.pipework{left:524px;top:398px;width:422px;height:422px;background:radial-gradient(circle at 50% 50%,#c98a5d 0,#9c8a74 45%,#6f6558 100%)}
  .services{position:absolute;left:478px;top:860px}
  .services-title{color:var(--blue-deep);font-size:38px;font-weight:900;letter-spacing:.3px;margin-bottom:22px}
  .services-title span{color:var(--blue)}
  .service-list{list-style:none}
  .service{display:flex;align-items:flex-start;color:var(--ink);font-size:27px;font-weight:500;line-height:33px;letter-spacing:.4px;text-transform:uppercase;margin-bottom:14px}
  .service svg{flex:none;width:28px;height:28px;margin:3px 28px 0 0}
  .footer{position:absolute;left:0;top:1286px;width:1053px;height:77px;background:linear-gradient(90deg,var(--blue-deep),var(--blue-light))}
  .contact-tab{position:absolute;left:0;top:-14px;width:256px;height:91px;border-radius:0 46px 46px 0;background:linear-gradient(90deg,var(--orange-deep),var(--yellow));display:flex;align-items:center;padding-left:24px;font-size:32px;font-weight:800;color:var(--ink)}
  .contact-list{position:absolute;top:12px;color:var(--white);font-size:15px;font-weight:700;line-height:27px;list-style:none}
  .contact-list li{display:flex;align-items:center;white-space:nowrap}
  .contact-list svg{width:16px;height:16px;margin-right:16px;flex:none}
  .contact-list.phones{left:284px}
  .contact-list.web{left:462px}
  .social{position:absolute;top:12px;right:22px;display:flex;flex-direction:column;gap:5px}
  .social span{display:flex;align-items:center;gap:7px;color:var(--white);font-size:14px;font-weight:700;line-height:22px;white-space:nowrap}
  .social i{display:block;width:20px;height:20px;border-radius:50%;background:var(--white)}
</style>
</head>
<body>
<main class="leaflet">
  <div class="leaflet-inner">
    <svg class="artwork" viewBox="0 0 1053 1363">
      <defs>
        <linearGradient id="heroPhoto" x1="0" y1="0" x2="1" y2="0">
          <stop offset="0" stop-color="#a7b8c0"/>
          <stop offset=".6" stop-color="#b9c0bd"/>
          <stop offset="1" stop-color="#d7d7d2"/>
        </linearGradient>
        <linearGradient id="heroTint" x1="0" y1="0" x2="1" y2="0">
          <stop offset="0" stop-color="#0b4f98" stop-opacity="1"/>
          <stop offset=".35" stop-color="#1367b4" stop-opacity=".85"/>
          <stop offset=".7" stop-color="#5fa8d6" stop-opacity="0"/>
        </linearGradient>
        <linearGradient id="orangeBand" x1="0" y1="0" x2="1" y2="1">
          <stop offset="0" stop-color="#fbb81c"/>
          <stop offset="1" stop-color="#f7731e"/>
        </linearGradient>
        <linearGradient id="redBand" x1="0" y1="0" x2="0" y2="1">
          <stop offset="0" stop-color="#f23d3d"/>
          <stop offset="1" stop-color="#ff6a4d"/>
        </linearGradient>
        <linearGradient id="arcBand" x1="0" y1="0" x2="1" y2="1">
          <stop offset="0" stop-color="#f05a28"/>
          <stop offset="1" stop-color="#fbb81c"/>
        </linearGradient>
      </defs>
      <g role="img" aria-label="Photo of a plumber in a hard hat fitting a water meter on a wall">
        <rect x="0" y="0" width="1053" height="760" fill="url(#heroPhoto)"/>
      </g>
      <rect x="0" y="0" width="1053" height="760" fill="url(#heroTint)"/>
      <path d="M1053,170 C1010,390 920,510 780,570 L1053,720 Z" fill="url(#redBand)"/>
      <path d="M0,400 C170,590 380,705 640,700 L640,1363 L0,1363 Z" fill="url(#orangeBand)"/>
      <path d="M0,505 C170,640 380,735 620,722 C790,712 930,640 1053,560 L1053,1363 L0,1363 Z" fill="#ffffff"/>
      <path d="M0,832 C240,815 390,950 405,1160 L392,1160 C368,980 230,872 0,878 Z" fill="url(#arcBand)"/>
      <g role="img" aria-label="Photo of an installed hot water cylinder and wall boiler with copper pipework">
        <path d="M0,878 C220,870 360,960 388,1140 L394,1290 L0,1290 Z" fill="#e7e8ea"/>
      </g>
    </svg>

    <div class="brand">
      <span class="brand-dot"></span>
      <span class="brand-name">BRACKENFOLD</span>
      <span class="brand-sub">PLUMBING SOLUTIONS</span>
    </div>

    <h1 class="headline">Don't let <strong>plumbing<br>problems</strong> slow you<br>down. Call <strong>Brackenfold<br>plumbing solutions</strong></h1>

    <div class="photo-frame boiler" role="img" aria-label="Photo of a wall mounted boiler with pipework on a wooden panel"></div>
    <div class="photo-frame pipework" role="img" aria-label="Photo of copper pipe runs laid between timber floor joists"></div>

    <section class="services">
      <h2 class="services-title">OUR <span>SERVICES</span></h2>
      <ul class="service-list">
        <li class="service"><svg viewBox="0 0 28 28"><circle cx="14" cy="14" r="11.5" fill="none" stroke="#1367b4" stroke-width="2.4" stroke-dasharray="58 14"/><path d="M8 14 l5 5 L25 6" fill="none" stroke="#1367b4" stroke-width="2.6" stroke-linecap="round" stroke-linejoin="round"/></svg><span>Boiler replacements<br>(free quote)</span></li>
        <li class="service"><svg viewBox="0 0 28 28"><circle cx="14" cy="14" r="11.5" fill="none" stroke="#1367b4" stroke-width="2.4" stroke-dasharray="58 14"/><path d="M8 14 l5 5 L25 6" fill="none" stroke="#1367b4" stroke-width="2.6" stroke-linecap="round" stroke-linejoin="round"/></svg><span>General plumbing &amp; heating</span></li>
        <li class="service"><svg viewBox="0 0 28 28"><circle cx="14" cy="14" r="11.5" fill="none" stroke="#1367b4" stroke-width="2.4" stroke-dasharray="58 14"/><path d="M8 14 l5 5 L25 6" fill="none" stroke="#1367b4" stroke-width="2.6" stroke-linecap="round" stroke-linejoin="round"/></svg><span>Tap replacements</span></li>
        <li class="service"><svg viewBox="0 0 28 28"><circle cx="14" cy="14" r="11.5" fill="none" stroke="#1367b4" stroke-width="2.4" stroke-dasharray="58 14"/><path d="M8 14 l5 5 L25 6" fill="none" stroke="#1367b4" stroke-width="2.6" stroke-linecap="round" stroke-linejoin="round"/></svg><span>1st &amp; 2nd</span></li>
        <li class="service"><svg viewBox="0 0 28 28"><circle cx="14" cy="14" r="11.5" fill="none" stroke="#1367b4" stroke-width="2.4" stroke-dasharray="58 14"/><path d="M8 14 l5 5 L25 6" fill="none" stroke="#1367b4" stroke-width="2.6" stroke-linecap="round" stroke-linejoin="round"/></svg><span>New builds &amp; extensions</span></li>
        <li class="service"><svg viewBox="0 0 28 28"><circle cx="14" cy="14" r="11.5" fill="none" stroke="#1367b4" stroke-width="2.4" stroke-dasharray="58 14"/><path d="M8 14 l5 5 L25 6" fill="none" stroke="#1367b4" stroke-width="2.6" stroke-linecap="round" stroke-linejoin="round"/></svg><span>Cylinder replcemets</span></li>
      </ul>
    </section>

    <footer class="footer">
      <div class="contact-tab">Contact Us</div>
      <ul class="contact-list phones">
        <li><svg viewBox="0 0 17 17"><rect x="4" y="1" width="9" height="15" rx="2" fill="none" stroke="#fff" stroke-width="1.8"/><circle cx="8.5" cy="13" r="1" fill="#fff"/></svg>07700 914226</li>
        <li><svg viewBox="0 0 17 17"><path d="M3 2 l3 0 1.5 4 -2 1.5 c1 2 2.5 3.5 4 4 l1.5 -2 4 1.5 0 3 c-7 1 -13 -5 -12 -12z" fill="#fff"/></svg>01632 870512</li>
      </ul>
      <ul class="contact-list web">
        <li><svg viewBox="0 0 17 17"><rect x="1" y="3" width="15" height="11" rx="1.5" fill="#fff"/><path d="M1.5 4 l7 5.5 7 -5.5" fill="none" stroke="#1367b4" stroke-width="1.4"/></svg>Info@brackenfoldplumbing.example.co.uk</li>
        <li><svg viewBox="0 0 17 17"><circle cx="8.5" cy="8.5" r="7" fill="none" stroke="#fff" stroke-width="1.6"/><ellipse cx="8.5" cy="8.5" rx="3" ry="7" fill="none" stroke="#fff" stroke-width="1.3"/><path d="M1.5 8.5 h14" stroke="#fff" stroke-width="1.3"/></svg>Brackenfold-plumbing.example.co.uk</li>
      </ul>
      <div class="social">
        <span><i></i>Chatterly</span>
        <span><i></i>pixgram</span>
      </div>
    </footer>
  </div>
</main>
</body>
</html>
```